Business Telephone Service Brochure

I need a brochure designed to help sell our VoIP service. The brochure needs to be clean, attention getting, professional and have 3 key areas of information (Key Features, Benefits & Service Plans). Here is an idea of what we are looking for https://www.artflockly.com/design/52930487. Need to also include how much the customer could save. See this for an example https://42mockups.com/postcard-flyer-design/contests/voip-sales-flyer-template-replicate-attached-358209. The Service Plan section needs to allow room for two types of plans. One plan includes the phone and has a 12, 24 and 36 month option. Each term (12,24,36) will have its own monthly cost per device. The second service option is no-commitment monthly with a single per month price per device. The included features section should allow for up to 16 features to be listed. The benefits should allow for 4-6 benefits to be listed. Also include room for Logo, business address, website, phone number and email.

Target Market(s)

Small to medium business with 1-100 employees.

Industry/Entity Type

Telecommunications

Font styles to use
Serif

Colors

Designer to choose colors to be used in the design.

Requirements
Must have
• Key Feature, Benefits and Service Plans (i.e. Pricing). Company logo, phone, email and website. Must have "Save up to x%!" and catch attention.
Nice to have
• Limited colors. I am not setting a hard limit, please take the liberty to do what you feel is needed. Just keep in mind we want it to be clean, professional and attention getting without being to flashy or obnoxious.
Should not have
• Nothing busy or distracting.

```html
<!DOCTYPE html>
<html lang="en">
<head>
<meta charset="utf-8">
<title>Veltra – Business Phone Service Flyer</title>
<link rel="stylesheet" href="https://fonts.googleapis.com/css2?family=Lato:wght@400;700;900&display=swap">
<style>
  :root {
    --navy: #262f7a;
    --blue: #1a5ba6;
    --blue-dark: #12468a;
    --ink: #1b1b2a;
    --paper: #ffffff;
    --stage: #e4e5e7;
    --photo-light: #f3f3f2;
    --photo-mid: #dcdcdc;
    --rule: #2a5fa8;
  }
  * { margin: 0; padding: 0; box-sizing: border-box; }
  html, body { width: 1200px; height: 590px; overflow: hidden; }
  body {
    background: var(--stage);
    font-family: "Lato", Arial, sans-serif;
    color: var(--ink);
    position: relative;
  }
  .flyer-frame {
    position: absolute;
    left: 372px; top: 0;
    width: 456px; height: 590px;
    overflow: hidden;
  }
  .flyer {
    position: absolute; left: 0; top: 0;
    width: 570px; height: 738px;
    transform: scale(0.8);
    transform-origin: 0 0;
    background: var(--paper);
    overflow: hidden;
  }
  .abs { position: absolute; }

  .hero-photo {
    left: 0; top: 0; width: 570px; height: 350px;
    background: linear-gradient(120deg, var(--photo-light) 0%, #fafafa 45%, var(--photo-mid) 100%);
  }
  .hero-shapes { left: 0; top: 0; width: 570px; height: 738px; }

  .brand { left: 18px; top: 14px; display: flex; align-items: center; gap: 10px; }
  .brand-dot { width: 18px; height: 18px; border-radius: 50%; background: var(--navy); }
  .brand-name { font-size: 72px; font-weight: 900; color: var(--navy); line-height: 1; letter-spacing: -1px; }
  .brand-tagline { left: 20px; top: 88px; font-size: 10px; color: var(--navy); letter-spacing: 0.2px; }

  .savings { left: 24px; top: 143px; color: var(--navy); }
  .savings-lead { font-size: 38px; font-weight: 400; line-height: 1; }
  .savings-figure { font-size: 76px; font-weight: 900; line-height: 1; margin-top: 2px; }

  .section-tag {
    height: 25px; padding: 0 18px 0 20px;
    background: var(--blue); color: #fff;
    font-size: 18px; font-weight: 700; line-height: 25px;
    border-radius: 0 13px 13px 0;
  }
  .tag-features { left: 0; top: 333px; width: 140px; }
  .tag-benefits { left: 310px; top: 333px; width: 103px; border-radius: 13px; }

  .bullet-list { list-style: none; font-size: 11.6px; line-height: 15.3px; }
  .bullet-list li { padding-left: 13px; position: relative; }
  .bullet-list li::before {
    content: ""; position: absolute; left: 1px; top: 5px;
    width: 5px; height: 5px; border-radius: 50%; background: var(--navy);
  }
  .features-list { left: 20px; top: 361px; }
  .benefits-list { left: 330px; top: 361px; }

  .values-panel {
    left: 298px; top: 460px; width: 272px; height: 95px;
    background: var(--blue-dark); color: #fff;
    font-size: 25px; font-weight: 900; line-height: 26px;
    text-align: center; padding-top: 9px;
  }

  .plan-table {
    left: 10px; top: 573px; width: 550px;
    border-collapse: collapse; font-size: 11px;
  }
  .plan-table th, .plan-table td { border: 1px solid var(--rule); }
  .plan-table thead th {
    background: var(--blue); color: #fff; font-size: 12.5px; font-weight: 700;
    height: 28px; text-align: center;
  }
  .plan-table thead th.plan-title {
    background: #fff; color: var(--navy); font-size: 16px; font-weight: 900;
    text-align: left; border: none; border-bottom: 1px solid var(--rule);
  }
  .plan-title span { color: var(--blue); }
  .plan-table thead th.col-monthly { background: var(--blue); }
  .plan-table thead th.col-term { background: var(--navy); }
  .plan-table td { height: 35px; }
  .plan-table td.plan-name { padding-left: 0; text-align: left; line-height: 12px; border-left: none; }
  .plan-table td.price { text-align: center; font-size: 17px; color: var(--navy); font-weight: 400; }
  .plan-table td:last-child { border-right: none; }
  .col-w1 { width: 130px; } .col-w2 { width: 75px; } .col-w3 { width: 113px; }
  .col-w4 { width: 115px; } .col-w5 { width: 117px; }

  .footer-band {
    left: 0; top: 686px; width: 570px; height: 52px;
    background: var(--navy); color: #fff;
  }
  .footer-top-rule { left: 0; top: 680px; width: 570px; height: 3px; background: var(--navy); }
  .pill {
    background: #fff; color: var(--navy); font-weight: 900;
    border-radius: 14px; height: 27px; line-height: 27px; text-align: center;
  }
  .phone-pill { left: 5px; top: 699px; width: 150px; font-size: 18px; }
  .web-pill { left: 416px; top: 699px; width: 148px; font-size: 14px; }
  .contact { left: 160px; top: 698px; width: 250px; text-align: center; color: #fff; font-size: 12px; line-height: 15px; }
</style>
</head>
<body>
<div class="flyer-frame">
  <article class="flyer">
    <div class="abs hero-photo" role="img" aria-label="Photo of hands holding a smartphone above a white office desk with papers and a calculator"></div>

    <svg class="abs hero-shapes" viewBox="0 0 570 738" aria-hidden="true">
      <polygon points="0,324 262,276 570,350 570,738 0,738" fill="#fff"/>
      <polyline points="0,324 262,276 570,350" fill="none" stroke="#262f7a" stroke-width="4"/>
      <polyline points="0,330 262,283 570,356" fill="none" stroke="#1a5ba6" stroke-width="1.5"/>
      <path d="M300,340 L310,333 L310,460 L300,460 Z" fill="#1a5ba6"/>
      <path d="M298,555 L312,555 L298,568 Z" fill="#12468a"/>
    </svg>

    <div class="abs brand"><span class="brand-name">veltra</span><span class="brand-dot"></span></div>
    <div class="abs brand-tagline">Internet-Telephone-Security-Networking</div>

    <div class="abs savings">
      <div class="savings-lead">Save up to</div>
      <div class="savings-figure">50 %!</div>
    </div>

    <div class="abs section-tag tag-features">Key Features</div>
    <ul class="abs bullet-list features-list">
      <li>Unlimited local and long distance calling</li>
      <li>HD Voice</li>
      <li>Business SMS/Text Messaging</li>
      <li>Personal and Shared Voicemail Boxes</li>
      <li>Audio Conferencing</li>
      <li>Intercom</li>
      <li>Mobile App</li>
      <li>Auto Attendant/Interactive Voice Routing</li>
      <li>Free web or email fax</li>
      <li>Web admin portal</li>
      <li>Music On Hold - Customizable</li>
      <li>Simultaneous ring / follow-me</li>
      <li>Redundancy/Failover – Never miss a call</li>
    </ul>

    <div class="abs section-tag tag-benefits">Benefits</div>
    <ul class="abs bullet-list benefits-list">
      <li>No expensive onsite telephone equipment</li>
      <li>Easily scale up or down and needs change</li>
      <li>Free telephone/email support</li>
      <li>Lower monthly cost</li>
      <li>Increase reliability</li>
      <li>Easy self-administration</li>
    </ul>

    <div class="abs values-panel">INTEGRITY<br>COMMITMENT<br>INNOVATION</div>

    <table class="abs plan-table">
      <colgroup><col class="col-w1"><col class="col-w2"><col class="col-w3"><col class="col-w4"><col class="col-w5"></colgroup>
      <thead>
        <tr>
          <th class="plan-title">SERVICE <span>PLAN</span></th>
          <th class="col-monthly">MONTHLY</th>
          <th class="col-term">12 MONTH TERM</th>
          <th class="col-term">24 MONTH TERM</th>
          <th class="col-term">36 MONTH TERM</th>
        </tr>
      </thead>
      <tbody>
        <tr>
          <td class="plan-name">1Phone service only<br>(phone sold separately)</td>
          <td class="price">$21.95</td><td></td><td></td><td></td>
        </tr>
        <tr>
          <td class="plan-name">Service + 2Norvik<br>N20 Phone</td>
          <td></td>
          <td class="price">$24.95</td><td class="price">$22.95</td><td class="price">$20.95</td>
        </tr>
      </tbody>
    </table>

    <div class="abs footer-top-rule"></div>
    <footer class="abs footer-band"></footer>
    <div class="abs pill phone-pill">555-014-7290</div>
    <div class="abs contact">PO Box 2041, Cedar Bend, OR 97000<br>hello@veltralink.net</div>
    <div class="abs pill web-pill">www.veltralink.net</div>
  </article>
</div>
</body>
</html>
```